Haventrix Corporate Stationery

Look for design of all new corporate stationery for an existing insurance broking business that is going through a redesign and move from older partners to younger family members. New Logo is attached. Company is Brisbane based.
Colours in the Logo is Hex #43bed8 and website features a lot of hex #17b8d8. Website front page "A plan to protect you" - headline. "Professional and Individual advice to protect your greatest assets" - tagline.

Stationery required: Business Cards, Letter head, Thank-you cards, Birthday cards, Presentation folders, With Compliment slips and a powerpoint template. We also would like to send a card to all customers with the something along of the lines of "something new".

Target Market(s)

Customers of Insurance business looking at superannuation, life and income protection insurance, investment advice and wills

Industry/Entity Type

Insurance Broker

Font styles to use
Other font styles liked:
• same as logo

Requirements
Must have
• The above designs for new stationery for the new business including:
• Business Cards, Letter head, Thank-you cards, Birthday cards, Presentation folders, With Compliment slips and a powerpoint template. We also would like to send a card to all customers with the something along of the lines of "something new".
Nice to have
• It is a new look - long time family business being passed to next generation - big focus on advice for YOU, individual advice etc..

```html
<!DOCTYPE html>
<html lang="en">
<head>
<meta charset="utf-8">
<title>Haventrix Corporate Stationery</title>
<link rel="stylesheet" href="https://fonts.googleapis.com/css2?family=Roboto+Condensed:wght@700&family=Source+Sans+3:wght@300;400;600&family=Great+Vibes&family=Cinzel:wght@700&display=swap">
<style>
:root{
  --teal:#43bed8;
  --sky:#17b8d8;
  --dark:#231f20;
  --deep:#1f6f80;
  --ink:#333;
  --grey:#6d6e71;
  --paper:#ffffff;
  --table:#e9ecee;
}
*{box-sizing:border-box;margin:0;padding:0}
html,body{width:1200px;height:1200px;overflow:hidden}
body{background:var(--table);font-family:"Source Sans 3",sans-serif;color:var(--ink);position:relative}
.piece{position:absolute;box-shadow:0 2px 8px rgba(0,0,0,.18)}
.brand{font-family:"Source Sans 3",sans-serif;font-weight:600;letter-spacing:.04em;display:flex;align-items:center;gap:8px;white-space:nowrap}
.brand .dot{display:inline-block;border-radius:50%;background:currentColor}
.band{background:var(--deep);color:#fff;text-align:center;font-size:12px;letter-spacing:.06em}

/* flyer */
.flyer{left:36px;top:40px;width:500px;height:400px;background:var(--dark);color:#fff;text-align:center}
.flyer .brand{justify-content:center;color:#fff;font-size:22px;margin-top:44px}
.flyer .brand .dot{width:14px;height:14px}
.flyer .web{font-size:10px;letter-spacing:.08em;margin-top:4px;color:#ddd}
.flyer h1{font-family:"Roboto Condensed",sans-serif;font-weight:700;color:var(--teal);font-size:40px;margin-top:62px;letter-spacing:.01em}
.flyer .tag{font-size:12px;margin-top:6px}
.flyer .body{font-size:9px;font-weight:300;line-height:1.65;margin:22px 44px 0}
.flyer .contact{position:absolute;left:0;right:0;bottom:34px;font-size:7.5px}
.flyer .band{position:absolute;left:0;right:0;bottom:0;height:26px;line-height:26px;background:#1e5f6e;font-size:10px}

/* folder */
.folder{left:560px;top:40px;width:600px;height:400px;background:linear-gradient(160deg,#3cc0da,#2aa9c6)}
.folder .brand{position:absolute;left:0;right:0;top:150px;justify-content:center;color:var(--dark);font-size:36px;font-weight:600}
.folder .brand .dot{width:26px;height:26px}
.folder .pocket{position:absolute;left:0;right:0;bottom:0;height:70px;background:rgba(0,0,0,.06);border-top:1px solid rgba(255,255,255,.25)}

/* letterhead */
.letter{left:36px;top:460px;width:504px;height:700px;background:var(--paper);font-size:10px}
.letter .head{position:absolute;left:14px;top:22px;right:0;display:flex;align-items:center}
.letter .head .brand{color:var(--teal);font-size:18px}
.letter .head .brand .dot{width:12px;height:12px}
.letter .head .band{flex:1;margin-left:10px;height:26px;line-height:26px;font-size:8.5px;letter-spacing:.2em;background:var(--teal);border-bottom:3px solid var(--deep)}
.letter .content{position:absolute;left:32px;right:30px;top:100px;line-height:1.55;text-align:justify}
.letter .content p{margin-bottom:12px}
.letter .sign{font-family:"Source Sans 3",sans-serif;font-style:italic;color:var(--teal);font-size:16px}
.letter .foot{position:absolute;right:24px;bottom:34px;font-size:9px;display:flex;gap:10px;text-align:right}
.letter .foot div + div{border-left:1px solid #aaa;padding-left:10px;text-align:left}
.letter .foot-band{position:absolute;left:150px;right:0;bottom:0;height:20px;background:var(--teal);border-top:3px solid var(--deep)}
.ico{display:inline-block;width:7px;height:7px;background:var(--teal);margin:0 3px;vertical-align:middle}

/* business cards */
.card{top:460px;width:280px;height:150px;background:var(--paper)}
.card.front{left:560px}
.card.back{left:860px;display:flex;align-items:center;justify-content:center}
.card.front .brand{position:absolute;left:14px;top:62px;color:var(--teal);font-size:15px}
.card .brand .dot{width:9px;height:9px}
.card.front .person{position:absolute;left:150px;top:16px}
.card.front .name{color:var(--teal);font-weight:600;font-size:11px}
.card.front .role{font-size:8px;color:var(--grey)}
.card.front .lines{position:absolute;left:150px;top:78px;font-size:7.5px;line-height:1.5}
.card.front .band{position:absolute;left:150px;right:0;bottom:0;height:12px;line-height:12px;font-size:4.5px;background:var(--teal)}
.card.back .brand{color:var(--teal);font-size:22px}

/* greeting cards */
.greet{top:630px;width:190px;height:180px;background:var(--teal);border:1px solid rgba(255,255,255,.5);color:#fff}
.greet .frame{position:absolute;inset:8px;border:1px solid rgba(255,255,255,.7)}
.thanks{left:560px;display:flex;flex-direction:column;align-items:center;justify-content:center}
.script{font-family:"Great Vibes",cursive;font-size:36px;line-height:1}
.thanks .please{font-size:9px;align-self:flex-end;margin-right:30px}
.birthday{left:762px}
.birthday .art{position:absolute;left:18px;top:18px;width:110px;height:90px;border-radius:40px;background:radial-gradient(circle at 40% 40%,#8fe4f3,#4cc6de)}
.birthday .script{position:absolute;right:18px;bottom:18px;font-size:24px;text-align:right}

/* something new */
.news{left:966px;top:630px;width:194px;height:270px;background:linear-gradient(150deg,#45c1da,#2eaac6);display:flex;align-items:center;justify-content:center}
.news .art{position:absolute;inset:0;background:radial-gradient(ellipse at 30% 30%,rgba(255,255,255,.18),transparent 60%)}
.news h2{position:relative;font-family:"Cinzel",serif;color:#fff;font-size:22px;text-align:center;line-height:1.4;letter-spacing:.05em}

/* compliment slip */
.slip{left:560px;top:920px;width:600px;height:240px;background:var(--paper)}
.slip .brand{position:absolute;left:24px;top:24px;color:var(--teal);font-size:22px}
.slip .brand .dot{width:14px;height:14px}
.slip h3{position:absolute;right:26px;top:118px;color:var(--teal);font-weight:600;font-size:22px;letter-spacing:.4em}
.slip .foot{position:absolute;right:26px;top:160px;font-size:10px;display:flex;gap:10px;text-align:right}
.slip .foot div + div{border-left:1px solid #aaa;padding-left:10px;text-align:left}
.slip .band{position:absolute;left:200px;right:0;bottom:0;height:34px;line-height:34px;font-size:9px;letter-spacing:.12em;background:var(--teal);border-top:3px solid var(--deep)}
</style>
</head>
<body>

<section class="piece flyer">
  <div class="brand"><span class="dot"></span>HAVENTRIX FINANCIAL GROUP</div>
  <div class="web">www.haventrixfinancial.com</div>
  <h1>A PLAN TO PROTECT YOU</h1>
  <p class="tag">Professional &amp; Individual advice to protect your greatest assets</p>
  <p class="body">Lorem Ipsum has been the industry's standard dummy text ever since the 1500s, when an unknown printer took a galley of type and scrambled it to make a type specimen book. It has survived not only five centuries but also the leap into electronic typesetting, remaining essentially unchanged. It was popularised in the 1960s with the release of Letraset sheets containing Lorem Ipsum passages, and more recently with desktop publishing software like Aldus PageMaker including versions of Lorem Ipsum</p>
  <p class="contact">T: 1-234-567890 | E: john@haventrixfinancial.com | Dummy city, Dummy Country Land</p>
  <div class="band">Authorised Representatives of Meridale AFS Licence No 418207</div>
</section>

<section class="piece folder">
  <div class="brand"><span class="dot"></span>HAVENTRIX FINANCIAL GROUP</div>
  <div class="pocket"></div>
</section>

<section class="piece letter">
  <header class="head">
    <div class="brand"><span class="dot"></span>HAVENTRIX</div>
    <div class="band">Authorised Representatives of Meridale AFS Licence No 418207</div>
  </header>
  <div class="content">
    <p>To<br>The,<br>Director</p>
    <p>Lorem ipsum dolor sit amet, consectetur adipiscing elit. Sed at ante. Mauris eleifend, quam a vulputate dictum, massa quam dapibus leo, eget vulputate orci purus ut lorem. In fringilla mi in ligula. Pellentesque aliquam quam vel dolor. Nunc adipiscing. Sed quam odio, tempus ac, aliquam molestie varius ac, tellus. Vestibulum ut nulla aliquam risus rutrum interdum. Pellentesque lorem.</p>
    <p>Curabitur sit amet erat quis risus feugiat viverra. Pellentesque augue justo, sagittis et, lacinia at, venenatis non, arcu. Nunc nec libero. In cursus dictum risus. Etiam tristique nisl a nulla. Ut a orci. Curabitur dolor nunc, egestas at, malesuada nec, magna. Nulla facilisi. Nunc volutpat. Vestibulum ante ipsum primis in faucibus orci luctus et ultrices posuere cubilia Curae.</p>
    <p>In hac habitasse platea dictumst. Ut consequat, tellus eu volutpat varius, justo orci elementum dolor, sed imperdiet nulla tellus ut diam. Vestibulum ipsum ante, malesuada quis, tempus ac, placerat sit amet, elit. Curabitur in odio.</p>
    <p>Thanking you,<br><span class="sign">John Doe</span></p>
  </div>
  <footer class="foot">
    <div>www.haventrixfinancial.com<span class="ico"></span><br>Dummy city, Dummy Country Land<span class="ico"></span></div>
    <div><span class="ico"></span>1-234-567890<br><span class="ico"></span>john@haventrixfinancial.com</div>
  </footer>
  <div class="foot-band"></div>
</section>

<section class="piece card front">
  <div class="person"><div class="name">JOHN DOE</div><div class="role">Director</div></div>
  <div class="brand"><span class="dot"></span>HAVENTRIX</div>
  <div class="lines">
    <div><span class="ico"></span>1-234-567890</div>
    <div><span class="ico"></span>www.haventrixfinancial.com</div>
    <div><span class="ico"></span>john@haventrixfinancial.com</div>
    <div><span class="ico"></span>Dummy city, Dummy Country Land</div>
  </div>
  <div class="band">Authorised Representatives of Meridale AFS Licence No 418207</div>
</section>

<section class="piece card back">
  <div class="brand"><span class="dot"></span>HAVENTRIX</div>
</section>

<section class="piece greet thanks">
  <div class="frame"></div>
  <div class="script">Thank You</div>
  <div class="please">please</div>
</section>

<section class="piece greet birthday">
  <div class="frame"></div>
  <div class="art" role="img" aria-label="Illustration of three blue balloons tied with a ribbon"></div>
  <div class="script">Happy<br>Birthday</div>
</section>

<section class="piece news">
  <div class="art" role="img" aria-label="Decorative swirling floral pattern in light blue"></div>
  <h2>SOMETHING<br>NEW</h2>
</section>

<section class="piece slip">
  <div class="brand"><span class="dot"></span>HAVENTRIX</div>
  <h3>WITH COMPLIMENTS</h3>
  <div class="foot">
    <div>www.haventrixfinancial.com<span class="ico"></span><br>Dummy city, Dummy Country Land<span class="ico"></span></div>
    <div><span class="ico"></span>1-234-567890<br><span class="ico"></span>john@haventrixfinancial.com</div>
  </div>
  <div class="band">Authorised Representatives of Meridale AFS Licence No 418207</div>
</section>

</body>
</html>
```